Business Card Design for Dovlan Holdings

I need a business card designed for Dovlan Holdings. I would like basic contact info and would like the card to be a bit modern but not childish. We manage several companies so it needs to look very professional. Watermark is cool and a plan logo maybe offset on the other side but I will leave the design up to you. I would like to see both color and grey scale designs. This is my first time using Sketch Harbor so hopefully we get some great results! Future projects available for the selected designer potentially.

Target Market(s)

Dovlan Holdings owns several companies serving the software, real estate and automotive industry

Industry/Entity Type

Business

Contact Information for Business Card

Gregory T. Dovlan
608.291.5537
gregory.t.dovlan@mailvista.example

Font styles to use
Serif

Requirements
Must have
• contact information listed on card details
Nice to have
• I am open to letting you use your creative mind to design the best eye catching cards.

```html
<!DOCTYPE html>
<html lang="en">
<head>
<meta charset="utf-8">
<title>Dovlan Holdings – Business Card</title>
<link rel="stylesheet" href="https://fonts.googleapis.com/css2?family=Lora:wght@500;600&family=Lato:wght@400;700&display=swap">
<style>
  :root {
    --bg: #3a3a3c;
    --brand-blue: #0a4fa0;
    --brand-blue-dark: #083f82;
    --accent-blue: #1f8fd6;
    --ink: #1c1c1c;
    --muted: #444;
    --card-white: #ffffff;
  }
  * { box-sizing: border-box; margin: 0; padding: 0; }
  html, body { width: 1200px; height: 814px; overflow: hidden; }
  body {
    background: var(--bg);
    display: flex;
    align-items: center;
    justify-content: center;
    gap: 40px;
    font-family: "Lato", sans-serif;
  }
  .card {
    position: relative;
    width: 540px;
    height: 310px;
    border-radius: 18px;
    overflow: hidden;
    box-shadow: 0 10px 30px rgba(0,0,0,.45);
  }
  .card-back {
    background: linear-gradient(160deg, var(--brand-blue) 0%, var(--brand-blue-dark) 100%);
    display: flex;
    align-items: center;
    justify-content: center;
    gap: 16px;
  }
  .back-mark-circle {
    width: 54px; height: 54px;
    border: 7px solid #fff;
    border-radius: 50%;
  }
  .back-name {
    font-family: "Lora", serif;
    font-weight: 600;
    font-size: 30px;
    color: #fff;
  }
  .card-front { background: var(--card-white); }
  .front-brand {
    position: absolute;
    left: 30px; top: 112px;
    display: flex; align-items: center; gap: 10px;
    white-space: nowrap;
  }
  .front-brand-circle {
    width: 40px; height: 40px;
    border-radius: 50%;
    background: var(--accent-blue);
  }
  .front-brand-name {
    font-family: "Lora", serif;
    font-weight: 600;
    font-size: 19px;
    color: var(--brand-blue);
  }
  .contact {
    position: absolute;
    left: 262px; top: 44px;
    white-space: nowrap;
    z-index: 2;
  }
  .contact-name {
    font-family: "Lora", serif;
    font-weight: 600;
    font-size: 21px;
    color: var(--ink);
  }
  .contact-title {
    font-size: 14px;
    color: var(--accent-blue);
    margin-bottom: 8px;
  }
  .contact-line {
    display: flex; align-items: center; gap: 7px;
    font-size: 11.5px;
    color: var(--muted);
    margin-top: 4px;
  }
  .contact-line svg { width: 11px; height: 11px; fill: var(--brand-blue); flex: none; }
  .wave { position: absolute; inset: 0; width: 100%; height: 100%; }
</style>
</head>
<body>
  <section class="card card-back">
    <div class="back-mark-circle"></div>
    <span class="back-name">Dovlan Holdings</span>
  </section>

  <section class="card card-front">
    <svg class="wave" viewBox="0 0 540 310" preserveAspectRatio="none" aria-hidden="true">
      <defs>
        <linearGradient id="silver" x1="0" y1="0" x2="1" y2="1">
          <stop offset="0" stop-color="#f2f2f2"/>
          <stop offset=".5" stop-color="#a9abae"/>
          <stop offset="1" stop-color="#e6e6e6"/>
        </linearGradient>
        <linearGradient id="blueBand" x1="0" y1="0" x2="1" y2="0">
          <stop offset="0" stop-color="#5fb0ea"/>
          <stop offset="1" stop-color="#0a4fa0"/>
        </linearGradient>
      </defs>
      <path d="M150 310 C230 215 340 262 430 238 C505 216 500 150 540 135 L540 310 Z" fill="url(#blueBand)"/>
      <path d="M166 310 C244 226 350 272 436 248 C510 228 508 164 540 152 L540 310 Z" fill="#fff"/>
      <path d="M174 310 C250 232 356 278 440 254 C514 234 512 172 540 160 L540 310 Z" fill="url(#silver)"/>
      <path d="M212 310 C280 258 376 296 460 268 C526 246 520 190 540 184 L540 310 Z" fill="#0b0b0b"/>
    </svg>

    <div class="front-brand">
      <div class="front-brand-circle"></div>
      <span class="front-brand-name">Dovlan Holdings</span>
    </div>

    <div class="contact">
      <p class="contact-name">Gregory T. Dovlan</p>
      <p class="contact-title">Managing Partner</p>
      <p class="contact-line">
        <svg viewBox="0 0 24 24"><path d="M6.6 10.8a15 15 0 0 0 6.6 6.6l2.2-2.2c.3-.3.7-.4 1-.2 1.1.4 2.3.6 3.6.6.6 0 1 .4 1 1V20c0 .6-.4 1-1 1A17 17 0 0 1 3 4c0-.6.4-1 1-1h3.5c.6 0 1 .4 1 1 0 1.3.2 2.5.6 3.6.1.3 0 .7-.2 1z"/></svg>
        608.291.5537
      </p>
      <p class="contact-line">
        <svg viewBox="0 0 24 24"><path d="M2 5h20v14H2zm2 2v.4l8 5 8-5V7zm0 2.8V17h16V9.8l-8 5z"/></svg>
        gregory.t.dovlan@mailvista.example
      </p>
    </div>
  </section>
</body>
</html>
```